Business Card Design

Need business card design for all carpentry & construction solutions. We would like to see designs that use black as a background with orange writing as it would stand out.

Business

KRV CONTRACTING
MARTIN COLBY
14 PELLINGTON ST
MERRIDALE
WA 6571
0498371265
krvcontracting@tramlex.com

```html
<!DOCTYPE html>
<html lang="en">
<head>
<meta charset="utf-8">
<title>KRV Contracting – Business Card</title>
<link rel="stylesheet" href="https://fonts.googleapis.com/css2?family=Montserrat:wght@500&family=Roboto:wght@400;700&display=swap">
<style>
  :root {
    --backdrop: #ececec;
    --orange: #e8501e;
    --black: #161617;
    --charcoal: #1e1e1e;
    --white: #ffffff;
    --text-light: #e6e6e6;
  }
  * { box-sizing: border-box; margin: 0; padding: 0; }
  html, body { width: 1200px; height: 800px; overflow: hidden; }
  body {
    background: var(--backdrop);
    position: relative;
    font-family: "Roboto", Arial, sans-serif;
  }
  .card {
    position: absolute;
    width: 460px;
    height: 264px;
    overflow: hidden;
    box-shadow: 0 6px 18px rgba(0,0,0,0.14);
  }
  /* Front */
  .card--front { left: 110px; top: 268px; background: var(--orange); }
  .front-band {
    position: absolute; left: 25%; width: 50%; top: 0; bottom: 0;
    background: var(--black);
    display: flex; align-items: center; justify-content: center;
  }
  .brand {
    display: flex; align-items: center; gap: 8px;
    font-family: "Montserrat", Arial, sans-serif;
    font-weight: 500; color: var(--orange);
    white-space: nowrap;
  }
  .brand-dot { width: 30px; height: 30px; border-radius: 50%; background: var(--orange); flex: none; }
  .card--front .brand-name { font-size: 15px; letter-spacing: 0.5px; }

  /* Back */
  .card--back { left: 630px; top: 268px; background: var(--charcoal); }
  .back-edge { position: absolute; left: 0; top: 0; bottom: 0; width: 36px; background: var(--charcoal); }
  .back-panel {
    position: absolute; left: 36px; top: 0; bottom: 0; width: 196px;
    background: var(--white);
    display: flex; align-items: center; justify-content: center;
  }
  .card--back .brand-name { font-size: 13px; letter-spacing: 0.3px; }
  .card--back .brand-dot { width: 26px; height: 26px; }
  .back-info { position: absolute; left: 232px; right: 0; top: 0; bottom: 0; }
  .name-bar {
    margin-top: 28px; height: 40px; background: var(--orange);
    display: flex; align-items: center; gap: 10px; padding-left: 12px;
    color: var(--white); font-weight: 700; font-size: 17px; letter-spacing: 0.3px;
    white-space: nowrap;
  }
  .name-bar svg { width: 16px; height: 16px; fill: var(--white); }
  .contacts { list-style: none; margin-top: 26px; }
  .contact {
    display: flex; align-items: flex-start; gap: 10px;
    color: var(--text-light); font-size: 11px; line-height: 1.3;
    margin-bottom: 14px;
  }
  .contact-icon {
    width: 34px; height: 22px; flex: none;
    background: var(--orange); border-radius: 0 11px 11px 0;
    display: flex; align-items: center; justify-content: center;
  }
  .contact-icon svg { width: 13px; height: 13px; fill: var(--white); }
  .contact-text { padding-top: 4px; white-space: nowrap; }
</style>
</head>
<body>
  <section class="card card--front" aria-label="Card front">
    <div class="front-band">
      <div class="brand">
        <span class="brand-dot"></span>
        <span class="brand-name">KRV CONTRACTING</span>
      </div>
    </div>
  </section>

  <section class="card card--back" aria-label="Card back">
    <div class="back-edge"></div>
    <div class="back-panel">
      <div class="brand">
        <span class="brand-dot"></span>
        <span class="brand-name">KRV CONTRACTING</span>
      </div>
    </div>
    <div class="back-info">
      <div class="name-bar">
        <svg viewBox="0 0 16 16" aria-hidden="true"><circle cx="8" cy="5" r="3.5"/><path d="M1.5 16c0-4 3-6 6.5-6s6.5 2 6.5 6z"/></svg>
        <span>MARTIN COLBY</span>
      </div>
      <ul class="contacts">
        <li class="contact">
          <span class="contact-icon"><svg viewBox="0 0 16 16" aria-hidden="true"><path d="M3.6 1.5l2.3 2.8-1.4 1.6c.9 1.9 2.4 3.4 4.3 4.4l1.6-1.4 2.8 2.3-1.3 2.3C6.8 13.3 2.5 9 2.5 3z"/></svg></span>
          <span class="contact-text">0498371265</span>
        </li>
        <li class="contact">
          <span class="contact-icon"><svg viewBox="0 0 16 16" aria-hidden="true"><path d="M8 1a7 7 0 100 14A7 7 0 008 1zm0 1.5c.7 0 1.6 1.5 1.9 4H6.1C6.4 4 7.3 2.5 8 2.5zM2.6 6.5h2.1c0-1.3.3-2.6.7-3.4A5.5 5.5 0 002.6 6.5zm0 3a5.5 5.5 0 002.8 3.4c-.4-.8-.7-2.1-.7-3.4zm3.5 0h3.8c-.3 2.5-1.2 4-1.9 4s-1.6-1.5-1.9-4zm5.2 0c0 1.3-.3 2.6-.7 3.4a5.5 5.5 0 002.8-3.4zm2.1-3a5.5 5.5 0 00-2.8-3.4c.4.8.7 2.1.7 3.4z"/></svg></span>
          <span class="contact-text">krvcontracting@tramlex.com</span>
        </li>
        <li class="contact">
          <span class="contact-icon"><svg viewBox="0 0 16 16" aria-hidden="true"><path d="M8 1a5 5 0 00-5 5c0 3.8 5 9 5 9s5-5.2 5-9a5 5 0 00-5-5zm0 7a2 2 0 110-4 2 2 0 010 4z"/></svg></span>
          <span class="contact-text">14 PELLINGTON ST<br>MERRIDALE<br>WA 6571</span>
        </li>
      </ul>
    </div>
  </section>
</body>
</html>
```